Foldable Wavelink Headphone Packaging Design

We would like a window box style packaging design for our Foldable Wavelink Headphone.

We want to use the packaging for 4-5 of our Wavelink headphone series (enclosed picture of the headphones for reference) and hence we would not like to put any product pictures on the packaging.
Material: E-Flute Paper box
Type: Window Box style
Design features we prefer: Colorful, creative, trendy, High tech.
Requirement: AI file is preferred
Size of Packaging: 170 (L) x 120 (W) x 200 (H) mm

Enclosed are a detailed description along with competitor designs for your reference.

Any further questions, please feel free to ask.

Target Market(s)

25-35 year olds

Industry/Entity Type

Electronics

Colors

Designer to choose colors to be used in the design.

Requirements
Must have
• Trendy Design

```html
<!DOCTYPE html>
<html lang="en">
<head>
<meta charset="utf-8">
<title>Foldable Wavelink Headphone – Window Box Dieline</title>
<link href="https://fonts.googleapis.com/css2?family=Archivo+Black&family=Open+Sans:wght@600;700;800&display=swap" rel="stylesheet">
<style>
  :root {
    --paper: #ffffff;
    --box-black: #05060a;
    --accent-blue: #2f6fe0;
    --bar-blue: #4a66c9;
    --fold-red: #9a1a1f;
    --cut-grey: #8a8a8a;
    --text-white: #ffffff;
    --text-grey: #6f6f6f;
  }
  html, body {
    margin: 0;
    padding: 0;
    width: 1200px;
    height: 1080px;
    overflow: hidden;
    background: var(--paper);
  }
  .dieline { display: block; width: 1200px; height: 1080px; }
  .cut-line { fill: none; stroke: var(--cut-grey); stroke-width: 0.8; }
  .fold-line { fill: none; stroke: var(--fold-red); stroke-width: 0.8; }
  .panel { fill: var(--box-black); }
  .title-text {
    font-family: "Archivo Black", "Arial Black", sans-serif;
    font-size: 26px;
    text-anchor: middle;
    fill: url(#silverText);
  }
  .spine-title {
    font-family: "Open Sans", Arial, sans-serif;
    font-weight: 800;
    font-size: 17px;
    fill: var(--text-white);
    text-anchor: middle;
  }
  .brand-name {
    font-family: "Open Sans", Arial, sans-serif;
    font-weight: 700;
    font-size: 9px;
    fill: var(--text-white);
  }
  .feature-heading, .feature-item {
    font-family: "Open Sans", Arial, sans-serif;
    font-weight: 700;
    font-size: 9.5px;
    fill: var(--text-white);
  }
  .spec-heading {
    font-family: "Open Sans", Arial, sans-serif;
    font-weight: 700;
    font-size: 8px;
    fill: var(--text-white);
  }
  .spec-item {
    font-family: "Open Sans", Arial, sans-serif;
    font-weight: 700;
    font-size: 7.5px;
    fill: var(--text-white);
  }
  .window-label {
    font-family: "Open Sans", Arial, sans-serif;
    font-weight: 600;
    font-size: 11px;
    letter-spacing: 3px;
    fill: var(--text-grey);
    text-anchor: middle;
  }
  .barcode-label {
    font-family: "Open Sans", Arial, sans-serif;
    font-weight: 700;
    font-size: 8px;
    fill: var(--text-grey);
    text-anchor: middle;
  }
  .legal-copy {
    font-family: "Open Sans", Arial, sans-serif;
    font-weight: 600;
    font-size: 4.6px;
    fill: var(--text-white);
  }
  .cert-badge { fill: none; stroke: var(--text-white); stroke-width: 0.5; }
</style>
</head>
<body>
<svg class="dieline" viewBox="0 0 1000 900" xmlns="http://www.w3.org/2000/svg">
  <defs>
    <linearGradient id="silverText" x1="0" y1="0" x2="0" y2="1">
      <stop offset="0" stop-color="#ffffff"/>
      <stop offset="1" stop-color="#9aa0c8"/>
    </linearGradient>
    <linearGradient id="blueBar" x1="0" y1="0" x2="1" y2="0">
      <stop offset="0" stop-color="#27346e"/>
      <stop offset="0.5" stop-color="#7f95e6"/>
      <stop offset="1" stop-color="#27346e"/>
    </linearGradient>
    <linearGradient id="specPill" x1="0" y1="0" x2="1" y2="0">
      <stop offset="0" stop-color="#6c7fe0"/>
      <stop offset="0.6" stop-color="#2f3f9a"/>
      <stop offset="1" stop-color="#2f3f9a" stop-opacity="0"/>
    </linearGradient>
    <radialGradient id="panelGlow" cx="0.5" cy="0.5" r="0.6">
      <stop offset="0" stop-color="#1d3f8f" stop-opacity="0.7"/>
      <stop offset="1" stop-color="#05060a" stop-opacity="0"/>
    </radialGradient>
    <radialGradient id="waveGlow" cx="0.55" cy="0.5" r="0.5">
      <stop offset="0" stop-color="#e8f4ff"/>
      <stop offset="0.25" stop-color="#4aa3ff"/>
      <stop offset="0.6" stop-color="#1a4fb8" stop-opacity="0.6"/>
      <stop offset="1" stop-color="#0a1a40" stop-opacity="0"/>
    </radialGradient>
    <radialGradient id="iconFill" cx="0.5" cy="0.5" r="0.5">
      <stop offset="0" stop-color="#dfe6ff"/>
      <stop offset="1" stop-color="#5e6fb4"/>
    </radialGradient>
    <clipPath id="bodyClip">
      <rect x="18" y="323" width="312" height="365"/>
      <rect x="330" y="318" width="186" height="350"/>
      <rect x="516" y="332" width="472" height="356"/>
    </clipPath>
  </defs>

  <!-- top tuck flap and dust flaps -->
  <path class="cut-line" d="M330 318 L355 250 H511"/>
  <path class="cut-line" d="M786 250 H945 L968 332"/>
  <g class="top-tuck">
    <rect class="panel" x="511" y="124" width="275" height="208"/>
    <rect x="511" y="124" width="275" height="208" fill="url(#panelGlow)"/>
    <g transform="rotate(180 648.5 228)">
      <line class="fold-line" x1="535" y1="283" x2="762" y2="283"/>
      <circle cx="530" cy="143" r="6" fill="#2f6fe0"/>
      <text class="brand-name" x="540" y="146">Wavelink</text>
      <text class="title-text" x="648" y="215" font-size="25">Foldable</text>
      <text class="title-text" x="648" y="245" font-size="25">Wavelink</text>
      <text class="title-text" x="648" y="275" font-size="25">Headphone</text>
    </g>
  </g>

  <!-- main body panels -->
  <rect class="panel" x="18" y="323" width="312" height="365"/>
  <rect class="panel" x="330" y="318" width="186" height="350"/>
  <rect class="panel" x="516" y="332" width="472" height="356"/>
  <g clip-path="url(#bodyClip)">
    <ellipse cx="430" cy="530" rx="120" ry="120" fill="url(#panelGlow)" opacity="0.5"/>
    <ellipse cx="860" cy="400" rx="110" ry="70" fill="url(#panelGlow)" opacity="0.6"/>
    <rect x="0" y="500" width="720" height="130" fill="url(#waveGlow)" role="img" aria-label="Glowing blue audio sound wave graphic"/>
  </g>

  <!-- fold lines -->
  <path class="fold-line" d="M66 358 H330 M66 668 H330 M66 358 V668"/>
  <path class="fold-line" d="M516 358 H988 M516 668 H988 M516 358 V668 M786 358 V668"/>

  <!-- bottom flaps -->
  <path class="cut-line" d="M78 688 L128 762 V805 H266 V762 L315 688"/>
  <path class="cut-line" d="M330 668 V805 H414 V748 L470 688"/>
  <path class="cut-line" d="M516 668 V805 H578 V762 H720 V805 H782 V668"/>
  <path class="cut-line" d="M805 688 L855 762 V805 H968 V688"/>

  <!-- side panel: specifications -->
  <g class="spec-panel">
    <line x1="176" y1="357" x2="216" y2="357" class="fold-line"/>
    <line x1="176" y1="382" x2="216" y2="382" class="fold-line"/>
    <rect x="47" y="393" width="96" height="12" rx="6" fill="url(#specPill)"/>
    <line x1="140" y1="399" x2="303" y2="399" stroke="#4a66c9" stroke-width="1.2"/>
    <text class="spec-heading" x="82" y="402">Specification:</text>
    <g>
      <circle cx="88" cy="413" r="2" fill="#fff"/><text class="spec-item" x="94" y="416">Wavelink Version: 5.0</text>
      <circle cx="88" cy="426" r="2" fill="#fff"/><text class="spec-item" x="94" y="429">Wireless Playback Duration: 10-12 h</text>
      <circle cx="88" cy="439" r="2" fill="#fff"/><text class="spec-item" x="94" y="442">Standby Time: 80 h</text>
      <circle cx="88" cy="452" r="2" fill="#fff"/><text class="spec-item" x="94" y="455">Wireless Range: 10 m</text>
      <circle cx="88" cy="465" r="2" fill="#fff"/><text class="spec-item" x="94" y="468">Impedance: 32 Ω</text>
      <circle cx="88" cy="478" r="2" fill="#fff"/><text class="spec-item" x="94" y="481">Sound Pressure Level: 100dB ± 3dB</text>
      <circle cx="88" cy="491" r="2" fill="#fff"/><text class="spec-item" x="94" y="494">Frequency Response: 20-20kHz</text>
      <circle cx="88" cy="504" r="2" fill="#fff"/><text class="spec-item" x="94" y="507">Plug Type: 3.5mm Stereo Detachable</text>
      <circle cx="88" cy="517" r="2" fill="#fff"/><text class="spec-item" x="94" y="520">Driver Unit: 40mm</text>
    </g>
    <rect x="79" y="620" width="66" height="43" fill="#ffffff"/>
    <text class="barcode-label" x="112" y="644">Barcode Here</text>
    <text class="legal-copy">
      <tspan x="150" y="627">Keep the headphones dry and away from heat. Charge fully</tspan>
      <tspan x="150" y="633">before first use. Fold gently at the hinges only. Store in</tspan>
      <tspan x="150" y="639">the box when not in use. Use the supplied cable for wired</tspan>
      <tspan x="150" y="645">listening. Made for daily music and calls.</tspan>
    </text>
    <g>
      <rect class="cert-badge" x="158" y="651" width="12" height="10"/>
      <rect class="cert-badge" x="178" y="651" width="12" height="10"/>
      <rect class="cert-badge" x="199" y="651" width="12" height="10"/>
      <rect class="cert-badge" x="220" y="651" width="12" height="10"/>
      <rect class="cert-badge" x="240" y="651" width="12" height="10"/>
      <rect class="cert-badge" x="261" y="651" width="12" height="10"/>
    </g>
  </g>

  <!-- narrow front panel -->
  <g class="front-panel">
    <rect x="345" y="373" width="163" height="4" rx="2" fill="url(#blueBar)"/>
    <rect x="345" y="443" width="163" height="4" rx="2" fill="url(#blueBar)"/>
    <circle cx="425" cy="410" r="27" fill="url(#iconFill)" opacity="0.85" role="img" aria-label="Headphone icon"/>
    <text class="title-text" x="425" y="492">Foldable</text>
    <text class="title-text" x="425" y="529">Wavelink</text>
    <text class="title-text" x="425" y="566">Headphone</text>
  </g>

  <!-- main window panel -->
  <g class="window-panel">
    <circle cx="566" cy="402" r="8" fill="#2f6fe0"/>
    <text class="brand-name" x="543" y="434">Wavelink</text>
    <path d="M650 396 H893 Q918 396 918 421 V607 Q918 632 893 632 H745 C680 620 630 560 625 480 V421 Q625 396 650 396 Z" fill="#ffffff"/>
    <text class="window-label" x="777" y="522">WINDOW</text>
    <text class="feature-heading" x="527" y="571">Features:</text>
    <text class="feature-item" x="527" y="591">• Wavelink V5</text>
    <text class="feature-item" x="527" y="606">• Foldable and Portable</text>
    <text class="feature-item" x="527" y="621">• Exceptional Sound Quality</text>
    <text class="feature-item" x="527" y="636">• Adjustable headband</text>
    <text class="feature-item" x="527" y="652">• Dual Mode wireless or wired connectivity</text>
  </g>

  <!-- side spine -->
  <text class="spine-title" transform="translate(953 515) rotate(-90)">Foldable Wavelink Headphone</text>
</svg>
</body>
</html>
```